Design a Flyer for Super Hero Day

Looking for a unique/cool flyer design for a kids super hero party.

I'll need an 8.5x11 flyer and a 4x6 matching in style image.

This should say: Fighting for Justice! Pursuing the Good! Striving for Awesome!

For any photos/images you need please use www.Pixelgrove.com I will purchase and attach any images for the winning designer. In the meantime, simply take a screen shot of the image you'd like to use, I understand the watermarks will be there, that's okay, we'll purchase the winning photos at the end.

Suggestions: Cool comic book style, maybe, mixed with a reality picture of a real kid?

I will need all photoshop work/source files in case there needs to be any edits, changes. There should be a space for a logo/day/date/time information. I appreciate if this can be incorporated INTO the design someway, and not just "added" if that makes sense.

Also, if you have questions post for clarification, I'll be quick to reply. Thank you :)

```html
<!DOCTYPE html>
<html lang="en">
<head>
<meta charset="UTF-8">
<title>Superhero Party Flyer</title>
<link href="https://fonts.googleapis.com/css2?family=Roboto+Condensed:wght@700&family=Russo+One&display=swap" rel="stylesheet">
<style>
  :root {
    --page-bg: #2a2a2a;
    --sky-top: #0d3f9a;
    --sky-mid: #2f7fe6;
    --sky-glow: #bfe6ff;
    --floor-top: #1b5fcf;
    --floor-bottom: #0a2a78;
    --panel: rgba(120, 170, 235, 0.35);
    --panel-edge: rgba(190, 220, 255, 0.35);
    --white: #ffffff;
    --text-shadow: rgba(5, 25, 80, 0.75);
    --chrome-light: #ffffff;
    --chrome-mid: #c9d0d8;
    --chrome-dark: #6d7682;
    --hero-red: #d0231d;
    --hero-blue: #3a58d8;
  }
  html, body {
    margin: 0;
    padding: 0;
    width: 893px;
    height: 1200px;
    overflow: hidden;
    background: var(--page-bg);
  }
  .flyer {
    position: relative;
    width: 893px;
    height: 1200px;
    overflow: hidden;
    background: linear-gradient(180deg, var(--sky-top) 0%, var(--sky-mid) 38%, var(--sky-glow) 50%, var(--floor-top) 52%, var(--floor-bottom) 100%);
  }
  .rays {
    position: absolute;
    inset: 0;
    width: 893px;
    height: 1200px;
  }
  .tagline-panel {
    position: absolute;
    left: 58px;
    right: 58px;
    top: 42px;
    height: 290px;
    border-radius: 10px;
    background: var(--panel);
    border: 1px solid var(--panel-edge);
    display: flex;
    flex-direction: column;
    justify-content: center;
    align-items: center;
  }
  .tagline {
    margin: 0;
    font-family: "Roboto Condensed", "Arial Narrow", sans-serif;
    font-weight: 700;
    font-size: 68px;
    line-height: 1.18;
    color: var(--white);
    text-align: center;
    text-shadow: 0 3px 6px var(--text-shadow);
  }
  .hero-art {
    position: absolute;
    left: 250px;
    top: 360px;
    width: 380px;
    height: 500px;
    border-radius: 40% 40% 20% 20%;
    background: radial-gradient(ellipse at 45% 45%, var(--hero-blue) 0%, var(--hero-red) 60%, rgba(208, 35, 29, 0) 75%);
    opacity: 0.85;
  }
  .event-title {
    position: absolute;
    left: 0;
    right: 0;
    top: 850px;
    margin: 0;
    text-align: center;
    font-family: "Russo One", "Arial Black", sans-serif;
    font-weight: 400;
    line-height: 0.98;
    text-transform: uppercase;
    background: linear-gradient(180deg, var(--chrome-light) 0%, var(--chrome-mid) 45%, var(--chrome-dark) 55%, var(--chrome-light) 100%);
    -webkit-background-clip: text;
    background-clip: text;
    color: transparent;
    filter: drop-shadow(0 4px 4px rgba(0, 0, 0, 0.6));
  }
  .event-title .line-one { display: block; font-size: 118px; }
  .event-title .line-two { display: block; font-size: 112px; }
  .event-details {
    position: absolute;
    left: 0;
    right: 0;
    top: 1090px;
    margin: 0;
    text-align: center;
    font-family: "Roboto Condensed", "Arial Narrow", sans-serif;
    font-weight: 700;
    font-size: 52px;
    color: var(--white);
    text-shadow: 0 3px 6px var(--text-shadow);
  }
</style>
</head>
<body>
  <main class="flyer">
    <svg class="rays" viewBox="0 0 893 1200" aria-hidden="true">
      <defs>
        <radialGradient id="centerGlow" cx="446" cy="600" r="420" gradientUnits="userSpaceOnUse">
          <stop offset="0" stop-color="#ffffff" stop-opacity="0.8"/>
          <stop offset="1" stop-color="#ffffff" stop-opacity="0"/>
        </radialGradient>
      </defs>
      <g fill="#ffffff" opacity="0.18">
        <polygon points="446,600 0,40 0,160"/>
        <polygon points="446,600 0,300 0,400"/>
        <polygon points="446,600 90,0 200,0"/>
        <polygon points="446,600 330,0 400,0"/>
        <polygon points="446,600 500,0 570,0"/>
        <polygon points="446,600 690,0 800,0"/>
        <polygon points="446,600 893,40 893,160"/>
        <polygon points="446,600 893,300 893,400"/>
      </g>
      <ellipse cx="446" cy="600" rx="420" ry="120" fill="url(#centerGlow)"/>
    </svg>

    <section class="tagline-panel">
      <p class="tagline">Fighting for Justice!<br>Pursuing the Good!<br>Striving for Awesome!</p>
    </section>

    <div class="hero-art" role="img" aria-label="Cartoon boy superhero in a blue suit with a yellow star and a red cape, hands on hips"></div>

    <h1 class="event-title">
      <span class="line-one">Superhero</span>
      <span class="line-two">Party</span>
    </h1>

    <p class="event-details">August 21, 2014 @ Some Place</p>
  </main>
</body>
</html>
```